Beacon Stewards Brochure Design*

We host a local leadership development program every two years. We need a brochure to promote the program. We would like it to be 8 1/2 x 11, tri-fold. I have attached a Word document with the necessary info for the brochure. The brochure will be professionally printed. We would like the final design to be in InDesign.

Target Market(s)

Potential participants of our leadership program. They will be local leaders, male and female, from 30-60 years of age.

Requirements
Must have
• Content as detailed in the Word document attached. Our logo.
Nice to have
• A design that is attractive to young professionals.

```html
<!DOCTYPE html>
<html lang="en">
<head>
<meta charset="utf-8">
<title>Beacon Stewards – Program Brochure</title>
<link rel="stylesheet" href="https://fonts.googleapis.com/css2?family=Quicksand:wght@400;700&family=Source+Sans+3:ital,wght@0,400;0,700;1,700&display=swap">
<style>
  :root{
    --teal-deep:#073f55;
    --teal:#0a4c66;
    --teal-mid:#0e6478;
    --teal-band:#0a3547;
    --white:#ffffff;
    --ink-blue:#16506a;
    --brand-navy:#2e3a8c;
  }
  *{box-sizing:border-box;margin:0;padding:0}
  html,body{width:1200px;height:927px;overflow:hidden;background:var(--white)}
  body{font-family:"Source Sans 3",Arial,sans-serif;color:var(--white)}
  .brochure{position:relative;width:1200px;height:927px;display:flex}
  .panel{position:relative;width:400px;height:927px;overflow:hidden}

  /* Left panel */
  .panel--details{background:var(--teal)}
  .photo-band{position:absolute;left:0;width:400px}
  .photo-band--top{top:0;height:320px;background:linear-gradient(180deg,#3f7588 0%,#1c5469 55%,var(--teal-deep) 100%)}
  .photo-band--bottom{bottom:0;height:180px;background:linear-gradient(0deg,#4d7f91 0%,#2a5e73 50%,var(--teal) 100%)}
  .divider{position:absolute;left:0;top:0}
  .section{position:absolute;left:44px;width:350px}
  .section h2{font-weight:400;font-size:29.5px;line-height:1;margin-bottom:16px;letter-spacing:.2px}
  .section p{font-size:13.2px;line-height:14.6px;white-space:nowrap}
  .section--attendance{top:160px}
  .section--tuition{top:353px}
  .section--apply{top:577px}
  .contact-box{position:absolute;left:0;top:773px;width:337px;height:65px;background:rgba(10,60,82,.6);padding:17px 0 0 44px;font-size:13.2px;line-height:14.6px}

  /* Middle panel */
  .panel--alumni{background:var(--teal)}
  .alumni-title{position:absolute;left:21px;top:108px;font-weight:400;line-height:.9}
  .alumni-title span{display:block;font-size:23px}
  .alumni-title strong{display:block;font-weight:400;font-size:30px}
  .testimonial{position:absolute;font-size:13.2px;line-height:17px}
  .testimonial p{white-space:nowrap}
  .testimonial--first{left:23px;top:207px}
  .testimonial--second{left:21px;top:508px}
  .testimonial .portrait{float:left;width:104px;height:135px;margin:0 5px 1px 0;background:linear-gradient(160deg,#9a9a9a,#4d4d4d)}
  .testimonial .quote{padding-top:2px}
  .testimonial .author{clear:both;margin-top:17px;font-weight:700;font-style:italic;font-size:13px;line-height:17px}

  /* Right panel */
  .panel--cover{background:var(--white)}
  .cover-art{position:absolute;left:0;top:0}
  .cover-quote{position:absolute;left:40px;top:94px;color:var(--ink-blue);font-family:"Quicksand","Source Sans 3",sans-serif;font-size:13.4px;line-height:17px;white-space:nowrap}
  .cover-quote b{font-weight:700;font-size:19.5px}
  .group-photo{position:absolute;left:0;top:277px;width:400px;height:233px;background:linear-gradient(180deg,#d8ccb0 0%,#b6a387 55%,#6f6660 100%)}
  .program-name{position:absolute;left:70px;top:716px;display:flex;align-items:center;gap:10px;color:var(--brand-navy);font-weight:700;font-size:31px;letter-spacing:.3px}
  .program-name i{display:block;width:26px;height:26px;border-radius:50%;background:var(--brand-navy)}
  .sponsors{position:absolute;right:41px;top:810px;text-align:right;color:var(--ink-blue);font-size:15.5px;line-height:18px}
  .sponsors small{display:block;font-size:12.5px;line-height:16px}
</style>
</head>
<body>
<main class="brochure">

  <section class="panel panel--details">
    <div class="photo-band photo-band--top" role="img" aria-label="Photo of professionals at a boardroom meeting, tinted teal"></div>
    <div class="photo-band photo-band--bottom" role="img" aria-label="Photo of a group of business people standing in an office, tinted teal"></div>
    <svg class="divider" width="400" height="927" aria-hidden="true">
      <polygon points="0,318 400,250 400,273 0,336" fill="var(--white)"/>
      <polygon points="0,491 400,604 400,620 0,517" fill="var(--white)"/>
    </svg>

    <div class="section section--attendance">
      <h2>Attendance Policy</h2>
      <p>Attendance at all sessions including the opening<br>retreat is compulsory. Participants may miss no more<br>than one session to graduate; however, the Organizational<br>Retreat is mandatory.</p>
    </div>
    <div class="section section--tuition">
      <h2>Tuition</h2>
      <p>If accepted in the Beacon Stewards program,<br>you or your employer/sponsor will be invoiced $400<br>for Chamber members and $500 for non-members.<br>This fee covers costs for the retreat, classroom<br>sessions, lunches, and graduation.<br>No refunds will be provided for participants who drop<br>out of the program or do not fulfill the required curriculum.</p>
    </div>
    <div class="section section--apply">
      <h2>To Apply</h2>
      <p>Applications are available on the Chamber’s website,<br>www.BeaconChamber.org Applications are due<br>by November 2, 2020.<br>Class size is limited.<br>All applications received by the deadline will be reviewed<br>and final participants for the Beacon Stewards class<br>will be contacted on December 4, 2020. However,<br>all applicants will be notified of the status of their<br>application in writing.</p>
    </div>
    <div class="contact-box">For questions,<br>please call the Chamber, 555-014-2283.</div>
  </section>

  <section class="panel panel--alumni">
    <h1 class="alumni-title"><span>What Community</span><strong>alumni are saying</strong></h1>

    <article class="testimonial testimonial--first">
      <div class="portrait" role="img" aria-label="Black and white portrait of alumna Dana Whitfield"></div>
      <p class="quote">“Beacon Stewards was an awesome<br>experience! I learned many interesting<br>things about the county that I have lived<br>in all my life. We had very informative<br>panel discussions and the tours of local<br>attractions, including the Millbrook<br>Correctional Facility were eye opening!<br>I enjoyed learning and working beside a<br>great group of folks who are taking leadership roles in our<br>communities to make our county a better place to live,<br>work and play.”</p>
      <p class="author">Dana Whitfield, Co-Owner, Harbor Smokehouse</p>
    </article>

    <article class="testimonial testimonial--second">
      <div class="portrait" role="img" aria-label="Black and white portrait of alumnus Owen R. Castell"></div>
      <p class="quote">“For the first year and a half I was working<br>at Castell Hart, I commuted from<br>Bayport, so I was not involved in the<br>community at all. Once we moved here,<br>I knew I wanted and felt I had to become<br>more involved. I learned about the program<br>through a colleague. I couldn’t have asked<br>for a better experience and it really exposed<br>me to the many ways that I could get involved and contribute<br>to the chamber and our community. I didn’t know a soul in that<br>2014 class when it started and now many of them are my very<br>best friends. If you have an opportunity to go through<br>Beacon Stewards you would be crazy to pass it up. It is the<br>best program the Chamber has and, quite frankly, one of the<br>best opportunities to better yourself in this community.</p>
      <p class="author">Owen R. Castell, CPA,<br>Partner/Manager of the Riverton Office<br>Castell Hart &amp; Associates, LLP</p>
    </article>
  </section>

  <section class="panel panel--cover">
    <svg class="cover-art" width="400" height="927" aria-hidden="true">
      <rect x="0" y="0" width="400" height="927" fill="var(--teal-mid)"/>
      <path d="M0,275 C150,250 330,170 400,0 L0,0 Z" fill="var(--teal-band)"/>
      <path d="M0,255 C160,235 330,150 390,0 L0,0 Z" fill="var(--white)"/>
      <path d="M0,765 C60,640 200,560 400,545 L400,927 L0,927 Z" fill="var(--teal-band)"/>
      <path d="M0,780 C70,665 210,570 400,552 L400,927 L0,927 Z" fill="var(--white)"/>
    </svg>
    <p class="cover-quote">“The <b>greatest wealth</b> of a<br>community lies not in the amount<br>of its treasure, but in the<br>quality of its <b>leadership</b>.”</p>
    <div class="group-photo" role="img" aria-label="Group photo of program alumni standing together in a meeting room beside a flag"></div>
    <div class="program-name"><i></i>BEACON STEWARDS</div>
    <p class="sponsors"><small>Sponsored by:</small>Lakeshore Community College<br>Beacon County Chamber of Commerce and Tourism</p>
  </section>

</main>
</body>
</html>
```